Brisbane IT support business needs our first business card

Hello we are a Brisbane based Information Technology company providing support and services to small and medium sized businesses. We provide a range of services and solutions.

The business name is Wattlebrook Network Computing Services, or WNCS for short.

I am looking for a business card that looks professional (don't we all want that), but most importantly, it most utilize the colours in the logo attached.

Reason: Launched late, extending so people have enough time to actually submit something.

Target Market(s)

Other business owners seeking our IT services, and also home users.

Industry/Entity Type

Business

Requirements
Must have
• Please only use the blue/orange colours in logo attached

```html
<!DOCTYPE html>
<html lang="en">
<head>
<meta charset="utf-8">
<title>WNCS Business Card</title>
<link href="https://fonts.googleapis.com/css2?family=Montserrat:wght@400;700&display=swap" rel="stylesheet">
<style>
  :root {
    --navy: #0d3d6e;
    --orange: #f26a10;
    --teal: #3f7d94;
    --teal-light: #8fb8c6;
    --faint: #e3ecec;
    --paper: #ffffff;
    --backdrop: #d5dcdb;
    --ink: #3a3f44;
  }
  * { box-sizing: border-box; margin: 0; padding: 0; }
  html, body { width: 1200px; height: 1000px; overflow: hidden; }
  body {
    background: var(--backdrop);
    font-family: "Montserrat", sans-serif;
    position: relative;
  }
  .card {
    position: absolute;
    width: 560px;
    height: 320px;
    background: var(--paper);
    overflow: hidden;
    box-shadow: 0 6px 18px rgba(0,0,0,0.12);
  }
  .card--back { left: 70px; top: 150px; }
  .card--front { left: 570px; top: 520px; }

  /* contact side */
  .back__emblem {
    position: absolute;
    left: 40px; top: 70px;
    width: 150px; height: 150px;
    border-radius: 50%;
    background: var(--faint);
  }
  .back__details {
    position: absolute;
    right: 34px; top: 40px;
    text-align: right;
    color: var(--ink);
    font-size: 15px;
    line-height: 1.7;
  }
  .back__name { color: var(--navy); font-weight: 700; font-size: 18px; }
  .back__role { font-weight: 400; font-size: 14px; color: var(--ink); }
  .back__band {
    position: absolute;
    left: 0; right: 0; bottom: 0;
    height: 78px;
    background: var(--orange);
    border-top: 6px solid var(--navy);
  }
  .back__web {
    position: absolute;
    left: 150px; top: 18px;
    color: #fff;
    font-weight: 700;
    font-size: 22px;
  }

  /* accent bars */
  .accent-bars { position: absolute; right: 0; display: flex; gap: 6px; }
  .accent-bars span { display: block; height: 8px; }
  .accent-bars .bar-dark { width: 70px; background: var(--teal); }
  .accent-bars .bar-mid { width: 40px; background: var(--teal); opacity: .75; }
  .accent-bars .bar-light { width: 30px; background: var(--teal-light); }
  .card--back .accent-bars { bottom: 84px; }
  .card--front .accent-bars { bottom: 30px; }
  .card--front .accent-bars span { height: 14px; }

  /* brand side */
  .front__brand {
    position: absolute;
    left: 70px; top: 105px;
    display: flex;
    align-items: center;
    gap: 22px;
  }
  .front__dot {
    flex: none;
    width: 100px; height: 100px;
    border-radius: 50%;
    background: var(--navy);
  }
  .front__name {
    color: var(--navy);
    font-weight: 700;
    font-size: 22px;
    line-height: 1.3;
    width: 300px;
  }
  .front__band {
    position: absolute;
    left: 0; right: 0; bottom: 0;
    height: 22px;
    background: var(--navy);
  }
</style>
</head>
<body>

  <section class="card card--back" aria-label="Business card, contact side">
    <div class="back__emblem"></div>
    <div class="back__details">
      <p><span class="back__name">Liam Hartley</span> <span class="back__role">manager</span></p>
      <p>48 Ferny Lane, Ashgrove 4060</p>
      <p>t: 3356 7821 / m: 0412 557 830</p>
      <p>e: info@wncs.com.au</p>
    </div>
    <div class="accent-bars">
      <span class="bar-dark"></span><span class="bar-mid"></span><span class="bar-light"></span>
    </div>
    <div class="back__band">
      <p class="back__web">www.wncs.com.au</p>
    </div>
  </section>

  <section class="card card--front" aria-label="Business card, brand side">
    <div class="front__brand">
      <div class="front__dot"></div>
      <p class="front__name">Wattlebrook Network Computing Services</p>
    </div>
    <div class="accent-bars">
      <span class="bar-dark"></span><span class="bar-mid"></span><span class="bar-light"></span>
    </div>
    <div class="front__band"></div>
  </section>

</body>
</html>
```